Präsentationsvorlagen
Zielgruppe
Wir sind ein Netzwerk aus unabhängigen Tierarztpraxen und-kliniken.
Aufgabenstellung
1. Allgemeine Anforderungen:
Wir benötigen ein Set an Masterfolien für unsere Präsentationen. Als Orientierung stellen wir Ihnen einige Beispielfolien im Anhang zur Verfügung, die eine grobe Vorstellung davon vermitteln, wie das Design aussehen soll. Zudem empfehlen wir, sich auf unserer Homepage umzusehen, um sicherzustellen, dass das Design mit unserem bestehenden Corporate Design harmoniert.
2. Farbkonzept:
Bitte verwenden Sie unsere definierten Unternehmensfarben:
Gelb: #f7cd4e
Blau: #143357
Gold: #9d8030
Weiß: #ffffff
3. Schriftarten:
Unsere Unternehmensschriftarten sind:
Raleway
Century Gothic
Bitte stellen Sie sicher, dass diese Fonts durchgehend verwendet werden.
4. Farbvarianten:
Wir wünschen uns drei unterschiedliche Farbvarianten der Masterfolien:
Blaue Version: mit Blau als dominierende Farbe
Gelbe Version: mit Gelb als dominierende Farbe
Neutrale Version: weiß dominierend mit - eine ausgewogene Mischung mit gedeckteren Farben
5. Design-Elemente:
Das Design sollte modern, professionell und klar strukturiert sein.
Die Masterfolien sollen verschiedene Layouts enthalten (Titelfolie, Inhaltsfolie, Bild-Text-Kombinationen, etc.).
Bitte achten Sie darauf, dass genügend weißer Raum für eine aufgeräumte und übersichtliche Gestaltung bleibt.
Elemente wie Linien, Icons oder dezente Muster können genutzt werden, sollten jedoch nicht zu dominant wirken.
6. Format:
Die Masterfolien sollten für Microsoft PowerPoint optimiert sein und in 16:9 Format erstellt werden.

```html
<!DOCTYPE html>
<html lang="de">
<head>
<meta charset="utf-8">
<title>Masterfolien – Übersicht</title>
<link href="https://fonts.googleapis.com/css2?family=Inter:wght@400;500;600;700&display=swap" rel="stylesheet">
<style>
  :root {
    --paper: #f5f4f0;
    --yellow: #efd16f;
    --navy: #1b3257;
    --page: #ffffff;
  }
  * { box-sizing: border-box; margin: 0; padding: 0; }
  html, body { width: 672px; height: 1200px; overflow: hidden; background: var(--page); }
  body { position: relative; font-family: "Inter", Arial, sans-serif; color: var(--navy); }

  .slide { position: absolute; width: 277px; height: 155px; background: var(--paper); overflow: hidden; }
  .slide--yellow { background: var(--yellow); }
  .col-left { left: 44px; }
  .col-right { left: 352px; }

  .brand { position: absolute; top: 13px; right: 16px; display: flex; align-items: center; gap: 2px;
           font-size: 6.6px; font-weight: 700; letter-spacing: 0.1px; color: var(--navy); }
  .brand-dot { width: 6px; height: 6px; border-radius: 50%; background: var(--navy); }

  .footer { position: absolute; left: 18px; right: 14px; top: 141px; border-top: 0.5px solid var(--yellow); }
  .footer-meta { position: absolute; top: 147px; left: 0; width: 277px; font-size: 2.4px; color: var(--yellow); }
  .footer-meta span { position: absolute; }
  .footer-meta .m1 { left: 206px; } .footer-meta .m2 { left: 229px; } .footer-meta .m3 { left: 261px; }

  .title-block { position: absolute; left: 18px; top: 44px; line-height: 1.15; }
  .title-block h2 { font-size: 13.5px; font-weight: 700; }
  .title-block p { font-size: 11px; font-weight: 400; }

  .accent { color: var(--yellow); }
  .circle { position: absolute; border-radius: 50%; background: var(--navy); }
  .bullets { list-style: none; font-size: 4px; line-height: 1.2; }
  .bullets li::before { content: "• "; }

  /* Titelfolie */
  .dot-field { position: absolute; border-radius: 50%;
               background: radial-gradient(circle, rgba(239,209,111,0.05) 25%, rgba(239,209,111,0.35) 60%, rgba(239,209,111,0.6) 100%); }
  .cover-title { position: absolute; left: 0; width: 282px; top: 60px; text-align: center; line-height: 1.05; }
  .cover-title h1 { font-size: 17.5px; font-weight: 700; }
  .cover-title p { font-size: 12px; }

  /* Agenda */
  .agenda-item { position: absolute; width: 85px; height: 19px; border: 0.8px solid var(--navy); border-radius: 2px;
                 display: flex; align-items: center; justify-content: space-between; padding: 0 6px 0 8px; }
  .agenda-item .label { font-size: 6px; }
  .agenda-item .num { font-size: 11px; }

  .body-copy { position: absolute; font-size: 7px; line-height: 7.6px; }
  .body-small { font-size: 3px; line-height: 3.4px; margin-top: 2px; }

  .card { position: absolute; width: 71px; height: 43px; background: var(--yellow); border-radius: 2px; padding: 6px 0 0 7px; }
  .card h3 { font-size: 5.5px; font-weight: 500; margin-bottom: 2px; }
  .card .circle { width: 22px; height: 22px; right: 5px; top: 11px; }

  .person { position: absolute; top: 46px; width: 55px; }
  .person .circle { position: relative; display: block; width: 22px; height: 22px; margin-left: 1px; }
  .person h3 { font-size: 5.7px; font-weight: 600; margin-top: 7px; }
  .person .role { font-size: 5.7px; margin-bottom: 4px; }

  .bar { position: absolute; width: 85px; height: 19px; background: var(--yellow); border-radius: 2px;
         display: flex; align-items: center; justify-content: space-between; padding: 0 6px 0 10px; }
  .bar .label { font-size: 6px; }
  .bar .num { font-size: 11px; }
  .bar .two-line { font-size: 4.5px; line-height: 1.05; }

  .date-band { position: absolute; left: 18px; top: 91px; width: 247px; height: 34px; background: var(--yellow); border-radius: 2px; }
  .date { position: absolute; top: 12px; display: flex; align-items: center; }
  .date .pair { display: flex; gap: 2px; margin-right: 4px; }
  .date .pair span { width: 13px; height: 13px; border-radius: 50%; background: var(--navy); }
  .date .txt { font-size: 5.6px; line-height: 1.1; }
  .date .txt b { font-weight: 600; display: block; }

  .step { position: absolute; width: 38px; height: 23px; background: var(--yellow); border-radius: 2px; padding: 3px 0 0 4px; }
  .step .n { font-size: 11px; line-height: 1; }
  .step .cap { font-size: 3.4px; font-weight: 700; margin-top: 3px; }
  .step-text { position: absolute; font-size: 3.4px; line-height: 3.6px; }

  .num-box { position: absolute; width: 24px; height: 19px; background: var(--yellow); border-radius: 2px;
             font-size: 11px; display: flex; align-items: center; justify-content: center; }
  .num-text { position: absolute; font-size: 4px; font-weight: 700; line-height: 4.4px; }

  .closing-field { position: absolute; left: -90px; top: -10px; width: 175px; height: 175px; border-radius: 50%;
                   background: radial-gradient(circle, rgba(27,50,87,0.35) 30%, rgba(27,50,87,0.15) 80%, rgba(27,50,87,0) 100%); }
  .closing-title { position: absolute; left: 105px; top: 55px; font-size: 17px; font-weight: 700; line-height: 1.15; }
</style>
</head>
<body>

<!-- 1 Titelfolie -->
<section class="slide col-left" style="top:45px">
  <div class="dot-field" role="img" aria-label="Kreisförmiges Punktmuster in Gelb" style="left:56px;top:-5px;width:164px;height:164px"></div>
  <div class="brand"><span class="brand-dot"></span>KLAROVENBERG</div>
  <div class="cover-title"><h1>Headline</h1><p>Subline</p></div>
</section>

<!-- 2 Agenda -->
<section class="slide slide--yellow col-right" style="top:45px">
  <div class="brand"><span class="brand-dot"></span>KLAROVENBERG</div>
  <div class="agenda-item" style="left:22px;top:34px"><span class="label">Unterpunkt</span><span class="num">1</span></div>
  <div class="agenda-item" style="left:114px;top:34px"><span class="label">Unterpunkt</span><span class="num">2</span></div>
  <div class="agenda-item" style="left:22px;top:58px"><span class="label">Unterpunkt</span><span class="num">3</span></div>
  <div class="agenda-item" style="left:114px;top:58px"><span class="label">Unterpunkt</span><span class="num">4</span></div>
  <div class="agenda-item" style="left:22px;top:82px"><span class="label">Unterpunkt</span><span class="num">5</span></div>
  <div class="agenda-item" style="left:114px;top:82px"><span class="label">Unterpunkt</span><span class="num">6</span></div>
  <div class="agenda-item" style="left:22px;top:107px"><span class="label">Unterpunkt</span><span class="num">7</span></div>
  <div class="agenda-item" style="left:114px;top:107px"><span class="label">Unterpunkt</span><span class="num">8</span></div>
</section>

<!-- 3 Text -->
<section class="slide col-left" style="top:227px">
  <div class="brand"><span class="brand-dot"></span>KLAROVENBERG</div>
  <div class="title-block"><h2>Unterpunkt</h2><p>Subline</p></div>
  <div class="body-copy" style="left:117px;top:48px;width:135px">
    Lorem ipsum dolor sit amet, consetetur <span class="accent">sadipscing</span> elitr, sed diam nonumy eirmod tempor invidunt ut labore et dolore magna aliquyam erat, sed diam voluptua. At vero eos et accusam et justo duo dolores <span class="accent">et ea rebum</span>. Stet clita kasd gubergren, no sea takimata sanctus est Lorem ipsum dolor sit amet.
    <p class="body-small">Lorem ipsum dolor sit amet, consetetur sadipscing elitr, sed diam nonumy eirmod tempor invidunt</p>
  </div>
  <div class="footer"></div>
  <div class="footer-meta"><span class="m1">Titel</span><span class="m2">Untertitel</span><span class="m3">3</span></div>
</section>

<!-- 4 Karten -->
<section class="slide col-right" style="top:227px">
  <div class="brand"><span class="brand-dot"></span>KLAROVENBERG</div>
  <div class="title-block"><h2>Unterpunkt</h2><p>Subline</p></div>
  <div class="card" style="left:112px;top:35px"><h3>Titel No. 1</h3><ul class="bullets"><li>Unterpunkt</li><li>Unterpunkt</li><li>Unterpunkt</li><li>Unterpunkt</li></ul><span class="circle"></span></div>
  <div class="card" style="left:190px;top:35px"><h3>Titel No. 2</h3><ul class="bullets"><li>Unterpunkt</li><li>Unterpunkt</li><li>Unterpunkt</li><li>Unterpunkt</li></ul><span class="circle"></span></div>
  <div class="card" style="left:112px;top:84px"><h3>Titel No. 3</h3><ul class="bullets"><li>Unterpunkt</li><li>Unterpunkt</li><li>Unterpunkt</li><li>Unterpunkt</li></ul><span class="circle"></span></div>
  <div class="card" style="left:190px;top:84px"><h3>Titel No. 4</h3><ul class="bullets"><li>Unterpunkt</li><li>Unterpunkt</li><li>Unterpunkt</li><li>Unterpunkt</li></ul><span class="circle"></span></div>
  <div class="footer"></div>
  <div class="footer-meta"><span class="m1">Titel</span><span class="m2">Untertitel</span><span class="m3">4</span></div>
</section>

<!-- 5 Team -->
<section class="slide col-left" style="top:408px">
  <div class="brand"><span class="brand-dot"></span>KLAROVENBERG</div>
  <div class="title-block"><h2>Unterpunkt</h2><p>Subline</p></div>
  <div class="person" style="left:108px"><span class="circle"></span><h3>Vor- und Zuname</h3><p class="role">Position</p><ul class="bullets"><li>Projekt 1</li><li>Projekt 2</li><li>Projekt 3</li><li>Projekt 4</li></ul></div>
  <div class="person" style="left:163px"><span class="circle"></span><h3>Vor- und Zuname</h3><p class="role">Position</p><ul class="bullets"><li>Projekt 1</li><li>Projekt 2</li><li>Projekt 3</li><li>Projekt 4</li></ul></div>
  <div class="person" style="left:218px"><span class="circle"></span><h3>Vor- und Zuname</h3><p class="role">Position</p><ul class="bullets"><li>Projekt 1</li><li>Projekt 2</li><li>Projekt 3</li><li>Projekt 4</li></ul></div>
  <div class="footer"></div>
  <div class="footer-meta"><span class="m1">Titel</span><span class="m2">Untertitel</span><span class="m3">5</span></div>
</section>

<!-- 6 Quartale -->
<section class="slide col-right" style="top:408px">
  <div class="brand"><span class="brand-dot"></span>KLAROVENBERG</div>
  <div class="title-block"><h2>Unterpunkt</h2><p>Subline</p></div>
  <div class="bar" style="left:113px;top:34px"><span class="label">Quartal</span><span class="num">1</span></div>
  <div class="bar" style="left:113px;top:57px"><span class="label">Quartal</span><span class="num">2</span></div>
  <div class="bar" style="left:113px;top:82px"><span class="label">Quartal</span><span class="num">3</span></div>
  <div class="bar" style="left:113px;top:107px"><span class="label">Quartal</span><span class="num">4</span></div>
  <ul class="bullets" style="position:absolute;left:204px;top:36px"><li>Projekt 1</li><li>Projekt 2</li><li>Projekt 3</li></ul>
  <ul class="bullets" style="position:absolute;left:204px;top:60px"><li>Projekt 1</li><li>Projekt 2</li><li>Projekt 3</li></ul>
  <ul class="bullets" style="position:absolute;left:204px;top:83px"><li>Projekt 1</li><li>Projekt 2</li><li>Projekt 3</li></ul>
  <ul class="bullets" style="position:absolute;left:204px;top:110px"><li>Projekt 1</li><li>Projekt 2</li><li>Projekt 3</li></ul>
  <div class="footer"></div>
  <div class="footer-meta"><span class="m1">Titel</span><span class="m2">Untertitel</span><span class="m3">6</span></div>
</section>

<!-- 7 Termine -->
<section class="slide col-left" style="top:604px">
  <div class="brand"><span class="brand-dot"></span>KLAROVENBERG</div>
  <div class="title-block"><h2>Termine</h2><p>Subline</p></div>
  <div class="date-band">
    <div class="date" style="left:21px"><span class="pair"><span></span><span></span></span><span class="txt"><b>TT.MM.JJ</b>Titel</span></div>
    <div class="date" style="left:92px"><span class="pair"><span></span><span></span></span><span class="txt"><b>TT.MM.JJ</b>Titel</span></div>
    <div class="date" style="left:163px"><span class="pair"><span></span><span></span></span><span class="txt"><b>TT.MM.JJ</b>Titel</span></div>
  </div>
  <div class="footer"></div>
  <div class="footer-meta"><span class="m1">Titel</span><span class="m2">Untertitel</span><span class="m3">7</span></div>
</section>

<!-- 8 Übersicht -->
<section class="slide col-right" style="top:604px">
  <div class="brand"><span class="brand-dot"></span>KLAROVENBERG</div>
  <div class="title-block"><h2>Übersicht</h2><p>Subline</p></div>
  <div class="bar" style="left:113px;top:33px"><span class="two-line">Einzeiler<br>Zweizeiler</span></div>
  <div class="bar" style="left:113px;top:57px"><span class="two-line">Einzeiler<br>Zweizeiler</span></div>
  <div class="bar" style="left:113px;top:81px"><span class="two-line">Einzeiler<br>Zweizeiler</span></div>
  <div class="bar" style="left:113px;top:107px"><span class="two-line">Einzeiler<br>Zweizeiler</span></div>
  <span class="circle" style="left:202px;top:34px;width:17px;height:17px"></span>
  <span class="circle" style="left:202px;top:58px;width:17px;height:17px"></span>
  <span class="circle" style="left:202px;top:82px;width:17px;height:17px"></span>
  <span class="circle" style="left:202px;top:108px;width:17px;height:17px"></span>
  <div class="footer"></div>
  <div class="footer-meta"><span class="m1">Titel</span><span class="m2">Untertitel</span><span class="m3">8</span></div>
</section>

<!-- 9 Schritte -->
<section class="slide col-left" style="top:799px">
  <div class="brand"><span class="brand-dot"></span>KLAROVENBERG</div>
  <div class="title-block"><h2>Unterpunkt</h2><p>Subline</p></div>
  <div class="body-copy" style="left:117px;top:48px;width:125px;font-size:4.8px;line-height:4.9px">
    Lorem ipsum dolor sit amet, consetetur <span class="accent">sadipscing</span> elitr, sed diam nonumy eirmod tempor invidunt ut labore et dolore magna aliquyam erat, sed diam voluptua. At vero eos et accusam et justo duo dolores <span class="accent">et ea rebum</span>. Stet clita kasd gubergren, no sea takimata sanctus est Lorem ipsum dolor sit amet.
  </div>
  <div class="step" style="left:112px;top:85px"><p class="n">01</p><p class="cap">Lorem ipsum dolor</p></div>
  <div class="step" style="left:160px;top:85px"><p class="n">02</p><p class="cap">Lorem ipsum dolor</p></div>
  <div class="step" style="left:208px;top:85px"><p class="n">03</p><p class="cap">Lorem ipsum dolor</p></div>
  <p class="step-text" style="left:117px;top:114px;width:35px">Lorem ipsum dolor sit amet, consetetur sadipscing elitr, sed diam nonumy eirmod tempor invidunt</p>
  <p class="step-text" style="left:164px;top:114px;width:35px">Lorem ipsum dolor sit amet, consetetur sadipscing elitr, sed diam nonumy eirmod tempor invidunt</p>
  <p class="step-text" style="left:212px;top:114px;width:35px">Lorem ipsum dolor sit amet, consetetur sadipscing elitr, sed diam nonumy eirmod tempor invidunt</p>
  <div class="footer"></div>
  <div class="footer-meta"><span class="m1">Titel</span><span class="m2">Untertitel</span><span class="m3">9</span></div>
</section>

<!-- 10 Thema -->
<section class="slide col-right" style="top:799px">
  <div class="brand"><span class="brand-dot"></span>KLAROVENBERG</div>
  <div class="title-block"><h2>Thema</h2><p>Warum?</p></div>
  <span class="circle" style="left:19px;top:86px;width:46px;height:46px"></span>
  <div class="step" style="left:112px;top:48px"><p class="n">01</p><p class="cap">Lorem ipsum dolor</p></div>
  <div class="step" style="left:112px;top:78px"><p class="n">02</p><p class="cap">Lorem ipsum dolor</p></div>
  <div class="step" style="left:112px;top:109px"><p class="n">03</p><p class="cap">Lorem ipsum dolor</p></div>
  <p class="step-text" style="left:157px;top:55px;width:72px">Lorem ipsum dolor sit amet, consetetur sadipscing elitr, sed diam nonumy eirmod tempor invidunt</p>
  <p class="step-text" style="left:157px;top:85px;width:72px">Lorem ipsum dolor sit amet, consetetur sadipscing elitr, sed diam nonumy eirmod tempor invidunt</p>
  <p class="step-text" style="left:157px;top:116px;width:72px">Lorem ipsum dolor sit amet, consetetur sadipscing elitr, sed diam nonumy eirmod tempor invidunt</p>
  <div class="footer"></div>
  <div class="footer-meta"><span class="m1">Titel</span><span class="m2">Untertitel</span><span class="m3">10</span></div>
</section>

<!-- 11 Nummerierte Liste -->
<section class="slide col-left" style="top:997px">
  <div class="brand"><span class="brand-dot"></span>KLAROVENBERG</div>
  <div class="title-block" style="top:46px"><h2>Headline</h2><p>Subline</p></div>
  <div class="num-box" style="left:91px;top:34px">01</div>
  <div class="num-box" style="left:91px;top:60px">02</div>
  <div class="num-box" style="left:91px;top:87px">03</div>
  <div class="num-box" style="left:91px;top:114px">04</div>
  <div class="num-box" style="left:178px;top:34px">05</div>
  <div class="num-box" style="left:178px;top:60px">06</div>
  <p class="num-text" style="left:119px;top:40px">Lorem ipsum dolor sit amet,<br>consetetur sadipscing elitr</p>
  <p class="num-text" style="left:119px;top:66px">Lorem ipsum dolor sit amet,<br>consetetur sadipscing elitr</p>
  <p class="num-text" style="left:119px;top:93px">Lorem ipsum dolor sit amet,<br>consetetur sadipscing elitr</p>
  <p class="num-text" style="left:119px;top:120px">Lorem ipsum dolor sit amet,<br>consetetur sadipscing elitr</p>
  <p class="num-text" style="left:208px;top:40px">Lorem ipsum dolor sit amet,<br>consetetur sadipscing elitr</p>
  <p class="num-text" style="left:208px;top:66px">Lorem ipsum dolor sit amet,<br>consetetur sadipscing elitr</p>
  <div class="footer"></div>
  <div class="footer-meta"><span class="m1">Titel</span><span class="m2">Untertitel</span><span class="m3">11</span></div>
</section>

<!-- 12 Abschluss -->
<section class="slide slide--yellow col-right" style="top:997px">
  <div class="closing-field" role="img" aria-label="Halbkreisförmiges Punktmuster in Blau und Gold"></div>
  <div class="brand"><span class="brand-dot"></span>KLAROVENBERG</div>
  <h2 class="closing-title">Lorem ipsum<br>dolor sit amet</h2>
</section>

</body>
</html>
```